Card Design Project

We are looking for a couple card / box designs that will for a new company that is in the bereavement assistance industry.
Our customers are churches, counseling centers and funeral homes.
Once we have these card designs we will need to work with that same artist to help us out with box graphic designs that are similar to the card designs. The box is 12" long x 4" wide x 6" high
We will need more designs in the future so we are looking for an artist for future work.
Our look needs to be professional and solemn.
The front of the card should be quite close to what i am attaching but with some professional touches to it that give it a proper look. We dont want you to stray to far from what i have attached but if you feel you have some good ideas we would be more than happy to see them.
The back of the card we want people to be able to leave the family a note so will need wording such as "leave a message to the family" or "write a memory"
Keep in mind we will need this look to be able to match graphics on the box as well, we kind of need the card design and box design to go together.
Thanks
Just wanted to mention to all designers that although we would like our logo on the card it is something that we need to keep kind of in the background somehow. We cant be seen as trying to push a brand name too much so please keep that in mind. Thanks
Reason: HOLIDAY
Designers, I took the need to see what the design looked like on a box out.
Reason: just need a bit of extra time guys, thanks for all who are helping us on this!
Target Market(s)
Funeral homes, churches, counseling centers
Industry/Entity Type
Industry
Requirements
Must have
- Professional and solemn look
Card need to be 4"wide X 6" high and needs to be portrait
A pin will be attached to the top right part of the card so will need a space there for it.
I was thinking that we would have the pic of the ribbon symbol there so when the pin is off the card there would still be a ribbon pic there. The pins that we will be attaching are ribbon pins similar to what i have on my pdf's
Please keep in mind that we cant really have out logo in a dominant area on the card. We would like to have it subtly in there but not to where it is in your face type of thing.
Nice to have
- Our logo but very small, not to intrusive .
Would like 2 designs, one dark and another light.
Maybe 1 masculine or gender neutral and another feminine
Wording should be the same

```html
<!DOCTYPE html>
<html lang="en">
<head>
<meta charset="utf-8">
<title>Memorial Pin Cards – Portrait, Reverse and Landscape</title>
<link rel="stylesheet" href="https://fonts.googleapis.com/css2?family=Cinzel:wght@400;600&display=swap">
<style>
  :root {
    --sheet: #ffffff;
    --teal-deep: #24574f;
    --teal-panel: rgba(33, 86, 78, 0.9);
    --teal-top: #3f7a7a;
    --peach: #efcf9f;
    --peach-light: #f3dcb2;
    --accent-yellow: #f2d200;
    --ink-light: #f4efe2;
    --ink-dark: #222222;
    --reverse-bg: #d9e5e4;
    --ribbon-grey: #a3a3a3;
    --rule-grey: #9a9a9a;
    --dot-grey: #8a8f8e;
  }
  * { box-sizing: border-box; margin: 0; padding: 0; }
  html, body { width: 900px; height: 1200px; overflow: hidden; background: var(--sheet); }
  .sheet { position: relative; width: 900px; height: 1200px; font-family: "Cinzel", serif; }

  .card { position: absolute; overflow: hidden; }
  .card--front { border: 1px solid #b89a72; }
  .card--portrait { left: 70px; top: 28px; width: 370px; height: 555px; }
  .card--landscape { left: 171px; top: 674px; width: 555px; height: 370px; }
  .card--reverse { left: 459px; top: 28px; width: 371px; height: 555px; background: var(--reverse-bg); }

  .artwork {
    position: absolute; inset: 0;
    background:
      radial-gradient(ellipse at 75% 60%, rgba(63,122,122,0.25), transparent 55%),
      linear-gradient(170deg, var(--teal-top) 0%, #8aa79a 16%, var(--peach-light) 38%, var(--peach) 70%, #e9c896 100%);
  }

  .message-panel {
    position: absolute; left: 0;
    background: var(--teal-panel);
    border-top: 3px solid var(--accent-yellow);
    border-bottom: 3px solid var(--accent-yellow);
    color: var(--ink-light);
    font-size: 12px; line-height: 14.6px; letter-spacing: 0.4px;
  }
  .card--portrait .message-panel { top: 122px; width: 202px; height: 313px; padding: 10px 0 0 34px; }
  .card--landscape .message-panel { top: 55px; width: 279px; height: 259px; padding: 22px 0 0 34px; }
  .message-panel p { margin-bottom: 14.6px; }

  .ribbon-spot { position: absolute; background: var(--ribbon-grey); border-radius: 18px 18px 4px 4px; }
  .card--portrait .ribbon-spot { left: 302px; top: 27px; width: 38px; height: 75px; }
  .card--landscape .ribbon-spot { left: 484px; top: 26px; width: 45px; height: 86px; }

  .brand-mark { position: absolute; text-align: center; color: var(--ink-dark); font-size: 8px; line-height: 9px; }
  .brand-mark__square { display: block; margin: 0 auto 3px; background: rgba(120,120,120,0.55); }
  .card--portrait .brand-mark { left: 300px; top: 480px; width: 46px; }
  .card--portrait .brand-mark__square { width: 30px; height: 30px; }
  .card--landscape .brand-mark { left: 482px; top: 296px; width: 46px; }
  .card--landscape .brand-mark__square { width: 30px; height: 30px; }

  .reverse-title { position: absolute; top: 92px; left: 0; width: 100%; text-align: center; font-size: 12.5px; color: var(--ink-dark); letter-spacing: 0.4px; }
  .write-line { position: absolute; left: 44px; width: 284px; border-top: 1.5px dotted var(--dot-grey); }
  .card--reverse .brand-mark { left: 145px; top: 459px; width: 80px; font-size: 11px; line-height: 12px; }
  .card--reverse .brand-mark__square { width: 52px; height: 50px; margin-bottom: 4px; }

  .sheet-rule { position: absolute; left: 38px; top: 1134px; width: 824px; border-top: 1px solid var(--rule-grey); }
</style>
</head>
<body>
<main class="sheet">

  <section class="card card--front card--portrait">
    <div class="artwork" role="img" aria-label="Distressed teal and peach texture with line-drawn poppies and hydrangea blossoms"></div>
    <div class="ribbon-spot" role="img" aria-label="Grey awareness ribbon marking the pin position"></div>
    <div class="message-panel">
      <p>Dear Friends</p>
      <p>Your support in<br>attending this<br>memorial and<br>celebration of life<br>means so much to us.</p>
      <p>Our loved one has<br>touched you in ways<br>we may not even<br>recognize yet.</p>
      <p>We invite you to wear<br>this pin through<br>your grieving process,<br>which we receive<br>as a symbol of your<br>sympathy and support<br>of our loss.</p>
    </div>
    <div class="brand-mark"><span class="brand-mark__square"></span>Quiet<br>Harbor</div>
  </section>

  <section class="card card--reverse">
    <h2 class="reverse-title">Leave a message to the family</h2>
    <div class="write-line" style="top:152px"></div>
    <div class="write-line" style="top:192px"></div>
    <div class="write-line" style="top:232px"></div>
    <div class="write-line" style="top:272px"></div>
    <div class="write-line" style="top:313px"></div>
    <div class="write-line" style="top:354px"></div>
    <div class="write-line" style="top:394px"></div>
    <div class="brand-mark"><span class="brand-mark__square"></span>Quiet<br>Harbor</div>
  </section>

  <section class="card card--front card--landscape">
    <div class="artwork" role="img" aria-label="Distressed teal and peach texture with line-drawn poppies and hydrangea blossoms"></div>
    <div class="ribbon-spot" role="img" aria-label="Grey awareness ribbon marking the pin position"></div>
    <div class="message-panel">
      <p>Dear Friends</p>
      <p>Your support in attending this<br>memorial and celebration of life<br>means so much to us.</p>
      <p>Our loved one has touched<br>you in ways we may not even<br>recognize yet.</p>
      <p>We invite you to wear this pin<br>through your grieving process,<br>which we receive as a symbol of<br>your sympathy and support of<br>our loss.</p>
    </div>
    <div class="brand-mark"><span class="brand-mark__square"></span>Quiet<br>Harbor</div>
  </section>

  <div class="sheet-rule"></div>
</main>
</body>
</html>
```